Service Plan Sales Flyer

The Watchpost Depot (www.kelvamart.com) is a commercial security integrator that installs security cameras, access control, intrusion, two-way radios and perimeter security. We require a one page flyer for our service plan for new and existing customers. The price of the service plan is $299/yr and includes the following;
1. Discounted service rate of $118/hr
2. Free remote support ($85/hr without a plan)
3. Free remote training
4. Priority support

Please review our brochure attached and create a one page sales flyer with the end goal of having the client sign up for our annual service plan . The plan will automatically renew every year. Email sales@kelvamart.com.

Target Market(s)

commercial industrial clients - no residential

Industry/Entity Type

review our website at www.kelvamart.com

Colors
0054AA
0677BA
7BADD7
CADEEF
E8F1F8
EE7325
F08F49
F5BC92
FAE3D3
FDF4ED

Requirements
Must have
• call to action
Should not have
• too many colors

```html
<!DOCTYPE html>
<html lang="en">
<head>
<meta charset="utf-8">
<title>The Watchpost Depot – Service Plan Flyer</title>
<link rel="stylesheet" href="https://fonts.googleapis.com/css2?family=Barlow+Condensed:ital,wght@0,700;0,800;1,800&family=Poppins:wght@400;500;600&display=swap">
<style>
  :root {
    --navy: #0d2a5c;
    --navy-deep: #0a2350;
    --red: #e8392d;
    --white: #ffffff;
    --rule: #e3e6ec;
    --backdrop: #c4c4c4;
    --line-soft: rgba(255,255,255,0.35);
  }
  * { margin: 0; padding: 0; box-sizing: border-box; }
  html, body { width: 931px; height: 1200px; overflow: hidden; }
  body { background: var(--backdrop); font-family: "Poppins", sans-serif; }

  .flyer {
    position: absolute; left: 63px; top: 29px;
    width: 731px; height: 1038px;
    background: var(--white);
    transform: scale(1.1); transform-origin: 0 0;
    overflow: hidden;
    box-shadow: 0 6px 14px rgba(0,0,0,0.25);
  }
  .panel-art { position: absolute; inset: 0; }
  .abs { position: absolute; }

  .brand { left: 40px; top: 52px; display: flex; align-items: center; gap: 10px; }
  .brand-dot { width: 22px; height: 22px; border-radius: 50%; background: var(--red); }
  .brand-name { font-family: "Barlow Condensed", sans-serif; font-weight: 800; font-size: 30px; color: var(--navy); text-transform: uppercase; letter-spacing: 0.5px; }

  .headline { left: 38px; top: 128px; font-family: "Barlow Condensed", sans-serif; font-weight: 800; font-size: 52px; line-height: 44px; color: var(--navy); letter-spacing: 0.5px; }
  .tag { display: flex; align-items: center; gap: 4px; }
  .slash { width: 9px; height: 100%; background: var(--red); transform: skewX(-14deg); }
  .tag-integrator { left: 42px; top: 226px; height: 40px; }
  .tag-integrator .label { background: var(--red); color: var(--white); font-family: "Barlow Condensed", sans-serif; font-style: italic; font-weight: 800; font-size: 28px; padding: 0 12px; height: 40px; line-height: 40px; margin-left: 6px; transform: skewX(-8deg); }

  .tag-install { left: 42px; top: 309px; height: 29px; }
  .tag-install .label { background: var(--navy); color: var(--white); font-family: "Barlow Condensed", sans-serif; font-weight: 800; font-size: 20px; padding: 0 10px; height: 29px; line-height: 29px; margin-right: 4px; transform: skewX(-8deg); }
  .tag-install .slash { background: var(--navy); width: 6px; }

  .install-list { left: 38px; top: 352px; width: 252px; list-style: none; }
  .install-list li { display: flex; align-items: center; gap: 13px; height: 84.5px; border-bottom: 1px solid var(--rule); }
  .install-list li:last-child { border-bottom: none; }
  .icon-ring { width: 58px; height: 58px; border-radius: 50%; background: var(--red); border: 3px solid var(--white); box-shadow: 0 0 0 2px var(--red); display: flex; align-items: center; justify-content: center; flex: none; }
  .install-list span { font-weight: 500; font-size: 17px; color: var(--navy-deep); }

  .plan-title { left: 38px; top: 776px; font-family: "Barlow Condensed", sans-serif; font-weight: 800; font-size: 23px; color: var(--navy); }
  .tag-price { left: 38px; top: 803px; height: 29px; }
  .tag-price .label { background: var(--red); color: var(--white); font-family: "Barlow Condensed", sans-serif; font-weight: 800; font-size: 24px; padding: 0 14px; height: 29px; line-height: 29px; margin-right: 6px; }
  .tag-price .slash { width: 6px; }
  .plan-includes { left: 202px; top: 800px; font-weight: 500; font-size: 13.5px; line-height: 16px; color: var(--navy-deep); text-transform: uppercase; }
  .benefits { left: 38px; top: 842px; width: 250px; list-style: none; font-size: 13.5px; color: var(--navy-deep); }
  .benefits li { display: flex; gap: 6px; line-height: 16px; margin-bottom: 8px; }
  .benefits svg { flex: none; margin-top: 2px; }
  .site-url { left: 38px; top: 970px; font-weight: 600; font-size: 24px; letter-spacing: 1px; color: var(--navy); }
  .site-url b { color: var(--red); font-weight: 600; }

  .product-visual { left: 400px; top: 48px; width: 312px; height: 208px; border-radius: 6px; background: linear-gradient(135deg, #e9ecef 0%, #c9ced6 55%, #8d949e 100%); }

  .tag-signup { left: 378px; top: 356px; height: 24px; }
  .tag-signup .label { background: var(--red); color: var(--white); font-family: "Barlow Condensed", sans-serif; font-weight: 800; font-size: 21px; padding: 0 15px; height: 24px; line-height: 24px; margin-right: 6px; }
  .tag-signup .slash { width: 5px; }
  .signup-note { left: 378px; top: 386px; font-size: 13px; line-height: 14.5px; color: var(--white); text-transform: uppercase; }
  .steps-count { left: 530px; top: 338px; font-family: "Barlow Condensed", sans-serif; font-weight: 800; font-size: 104px; line-height: 104px; color: var(--red); }
  .steps-title { left: 588px; top: 350px; font-family: "Barlow Condensed", sans-serif; font-weight: 800; font-size: 42px; line-height: 38px; color: var(--white); }

  .step { left: 378px; width: 318px; height: 86px; border: 1px solid var(--line-soft); border-radius: 8px; color: var(--white); }
  .step-num { position: absolute; left: 10px; top: 6px; font-family: "Barlow Condensed", sans-serif; font-weight: 800; font-size: 44px; line-height: 46px; color: var(--red); }
  .step-title { position: absolute; left: 42px; top: 8px; font-weight: 400; font-size: 15px; line-height: 17px; text-transform: uppercase; }
  .step-text { position: absolute; left: 12px; right: 12px; bottom: 8px; font-size: 12.5px; line-height: 14px; }
</style>
</head>
<body>
<main class="flyer">
  <svg class="panel-art" width="731" height="1038" viewBox="0 0 731 1038" aria-hidden="true">
    <path d="M340 150 L575 33 L731 150 L731 1038 L340 1038 Z" fill="#0d2a5c"/>
    <path d="M340 178 L580 298 L731 240 L731 262 L580 325 L340 212 Z" fill="#ffffff"/>
    <path d="M622 108 L731 163 L622 225 Z" fill="#e8392d"/>
  </svg>

  <div class="abs brand"><span class="brand-dot"></span><span class="brand-name">The Watchpost Depot</span></div>

  <h1 class="abs headline">COMMERCIAL<br>SECURITY</h1>
  <div class="abs tag tag-integrator"><i class="slash"></i><i class="slash"></i><i class="slash"></i><span class="label">INTEGRATOR</span></div>

  <div class="abs tag tag-install"><span class="label">WE INSTALL</span><i class="slash"></i><i class="slash"></i><i class="slash"></i></div>

  <ul class="abs install-list">
    <li><span class="icon-ring"><svg width="30" height="30" viewBox="0 0 30 30"><rect x="6" y="8" width="16" height="9" rx="2" fill="#fff" transform="rotate(20 14 12)"/><path d="M5 22 h6 v-5" stroke="#fff" stroke-width="2.5" fill="none"/></svg></span><span>Security Cameras</span></li>
    <li><span class="icon-ring"><svg width="30" height="30" viewBox="0 0 30 30"><circle cx="15" cy="6" r="3" fill="#fff"/><path d="M6 11 h18 M15 11 v8 M15 19 l-5 7 M15 19 l5 7" stroke="#fff" stroke-width="3" stroke-linecap="round" fill="none"/></svg></span><span>Access control</span></li>
    <li><span class="icon-ring"><svg width="30" height="30" viewBox="0 0 30 30"><circle cx="15" cy="15" r="10" stroke="#fff" stroke-width="2.5" fill="none"/><path d="M15 9 v7" stroke="#fff" stroke-width="3" stroke-linecap="round"/><circle cx="15" cy="20.5" r="1.7" fill="#fff"/></svg></span><span>Intrusion</span></li>
    <li><span class="icon-ring"><svg width="30" height="30" viewBox="0 0 30 30"><rect x="4" y="10" width="22" height="14" rx="2" stroke="#fff" stroke-width="2.5" fill="none"/><circle cx="11" cy="17" r="3" fill="#fff"/><path d="M17 15 h6 M17 19 h6 M8 10 l12 -5" stroke="#fff" stroke-width="2"/></svg></span><span>Two-way radios</span></li>
    <li><span class="icon-ring"><svg width="30" height="30" viewBox="0 0 30 30"><path d="M15 4 L24 8 V15 C24 21 20 25 15 27 C10 25 6 21 6 15 V8 Z" stroke="#fff" stroke-width="2.5" fill="none"/><rect x="11" y="14" width="8" height="7" rx="1" fill="#fff"/><path d="M12.5 14 v-2 a2.5 2.5 0 0 1 5 0 v2" stroke="#fff" stroke-width="2" fill="none"/></svg></span><span>Perimeter security</span></li>
  </ul>

  <h2 class="abs plan-title">SERVICE PLAN</h2>
  <div class="abs tag tag-price"><span class="label">$299/YR</span><i class="slash"></i><i class="slash"></i><i class="slash"></i></div>
  <p class="abs plan-includes">And includes<br>the following</p>
  <ul class="abs benefits">
    <li><svg width="13" height="13" viewBox="0 0 13 13"><rect x="1" y="2" width="10" height="10" rx="1.5" stroke="#e8392d" stroke-width="1.5" fill="none"/><path d="M3.5 7 l2.3 2.3 L12 2" stroke="#e8392d" stroke-width="1.8" fill="none"/></svg>Discounted service rate of $118/hr</li>
    <li><svg width="13" height="13" viewBox="0 0 13 13"><rect x="1" y="2" width="10" height="10" rx="1.5" stroke="#e8392d" stroke-width="1.5" fill="none"/><path d="M3.5 7 l2.3 2.3 L12 2" stroke="#e8392d" stroke-width="1.8" fill="none"/></svg>Free remote support ($85/hr without a plan)</li>
    <li><svg width="13" height="13" viewBox="0 0 13 13"><rect x="1" y="2" width="10" height="10" rx="1.5" stroke="#e8392d" stroke-width="1.5" fill="none"/><path d="M3.5 7 l2.3 2.3 L12 2" stroke="#e8392d" stroke-width="1.8" fill="none"/></svg>Free remote training</li>
    <li><svg width="13" height="13" viewBox="0 0 13 13"><rect x="1" y="2" width="10" height="10" rx="1.5" stroke="#e8392d" stroke-width="1.5" fill="none"/><path d="M3.5 7 l2.3 2.3 L12 2" stroke="#e8392d" stroke-width="1.8" fill="none"/></svg>Priority support</li>
  </ul>
  <p class="abs site-url">www.<b>kelvamart</b>.com</p>

  <div class="abs product-visual" role="img" aria-label="Product photo of a door with access reader, a monitor showing camera footage, a dome camera and a bullet camera"></div>

  <div class="abs tag tag-signup"><span class="label">SIGN UP</span><i class="slash"></i><i class="slash"></i><i class="slash"></i></div>
  <p class="abs signup-note">For our annual<br>subscription plan<br>with this</p>
  <div class="abs steps-count">5</div>
  <h2 class="abs steps-title">EASY<br>STEPS</h2>

  <section class="abs step" style="top:460px"><span class="step-num">1</span><h3 class="step-title">Needs<br>Consultation</h3><p class="step-text">Our process offers you total security coverage</p></section>
  <section class="abs step" style="top:566px"><span class="step-num">2</span><h3 class="step-title">Custom<br>Quote2</h3><p class="step-text">A quote that fits your security needs Whatever they are.</p></section>
  <section class="abs step" style="top:672px"><span class="step-num">3</span><h3 class="step-title" style="top:16px">Installation</h3><p class="step-text" style="bottom:14px">We'll make installation worry free</p></section>
  <section class="abs step" style="top:778px"><span class="step-num">4</span><h3 class="step-title">Ongoing<br>Support</h3><p class="step-text" style="bottom:12px">Our customer service is second to none.</p></section>
  <section class="abs step" style="top:884px"><span class="step-num">5</span><h3 class="step-title">Improvements &amp;<br>Updates</h3><p class="step-text">We keep you informed about improvements to your system.</p></section>
</main>
</body>
</html>
```